Business Card and Stationary Design for Solstice Land Company
Solstice Land Partners
Business Card and Stationary Design for Solstice Land Company - Real Estate
Creative Brief
Use same font as used in my logo
Tobias "TK" Kalder
Realtor
2876 Mellow Crest Lane Irvine, CA 92611
tk@TheSolsticeLP.example
www.TheSolsticeLP.example
BRE Lic: 07326159
We need the following design work done: Business Cards, Presentation Folder, Letterhead, Envelopes. We will upload our logo and the design templates from our print shop for all the above items needed in order to print correctly. Business Cards (Front & Back): 4 color both sides. Presentation Folder - (Front, Back and inside) 4 colors all sides, including business card slit inside.
We will upload pictures of sample business cards (Front and Back) that we like from competitor companies.

```html
<!DOCTYPE html>
<html lang="en">
<head>
<meta charset="utf-8">
<title>Solstice Land Partners — Business Card</title>
<link rel="stylesheet" href="https://fonts.googleapis.com/css2?family=Open+Sans:wght@400;600;700&display=swap">
<style>
  :root {
    --backdrop: #e6e7e9;
    --card: #ffffff;
    --ink: #2b2b2b;
    --ink-soft: #4a4a4a;
    --teal: #1fb5c4;
    --teal-deep: #1597a6;
    --black: #111111;
    --white: #ffffff;
  }
  * { margin: 0; padding: 0; box-sizing: border-box; }
  html, body {
    width: 1200px;
    height: 816px;
    overflow: hidden;
    background: var(--backdrop);
    font-family: "Open Sans", Arial, sans-serif;
  }
  .business-card {
    position: absolute;
    left: 100px;
    top: 122px;
    width: 1000px;
    height: 572px;
    background: var(--card);
    border-radius: 40px;
    overflow: hidden;
    box-shadow: 0 6px 18px rgba(0,0,0,0.12);
  }
  .card-shapes {
    position: absolute;
    inset: 0;
  }
  .brand {
    position: absolute;
    right: 60px;
    top: 156px;
    display: flex;
    align-items: center;
    gap: 16px;
  }
  .brand-square {
    width: 34px;
    height: 34px;
    background: var(--teal);
  }
  .brand-name {
    font-size: 40px;
    font-weight: 700;
    color: var(--ink);
    letter-spacing: -0.5px;
  }
  .holder {
    position: absolute;
    left: 78px;
    top: 188px;
  }
  .holder-name {
    font-size: 30px;
    font-weight: 600;
    color: var(--ink);
    text-transform: uppercase;
    letter-spacing: 0.5px;
  }
  .holder-title {
    font-size: 24px;
    color: var(--teal-deep);
    margin-top: 2px;
  }
  .contact-list {
    position: absolute;
    left: 78px;
    top: 326px;
    list-style: none;
    color: var(--ink-soft);
    font-size: 21px;
    line-height: 28px;
  }
  .contact-item {
    display: flex;
    align-items: flex-start;
    gap: 12px;
    margin-bottom: 4px;
  }
  .contact-item--address { font-weight: 600; color: var(--ink); }
  .contact-icon {
    width: 18px;
    height: 18px;
    margin-top: 5px;
    flex: none;
    fill: var(--teal-deep);
  }
  .website {
    position: absolute;
    left: 556px;
    top: 374px;
    width: 424px;
    line-height: 36px;
    text-align: center;
    font-size: 26px;
    font-weight: 600;
    color: var(--white);
    letter-spacing: 0.2px;
    white-space: nowrap;
  }
</style>
</head>
<body>
  <div class="business-card">
    <svg class="card-shapes" width="1000" height="572" viewBox="0 0 1000 572" aria-hidden="true">
      <path d="M0 508 C 300 506, 560 478, 1000 432 L1000 572 L0 572 Z" fill="var(--teal)"/>
      <path d="M0 508 C 300 506, 560 478, 1000 432 L1000 442 C 560 488, 300 516, 0 518 Z" fill="var(--teal-deep)"/>
      <rect x="536" y="354" width="500" height="78" rx="39" fill="var(--black)"/>
    </svg>

    <div class="brand">
      <span class="brand-square"></span>
      <span class="brand-name">Solstice Land Partners</span>
    </div>

    <div class="holder">
      <p class="holder-name">Tobias "TK" Kalder</p>
      <p class="holder-title">Realtor</p>
    </div>

    <ul class="contact-list">
      <li class="contact-item contact-item--address">
        <svg class="contact-icon" viewBox="0 0 24 24"><path d="M12 2a7 7 0 0 0-7 7c0 5.2 7 13 7 13s7-7.8 7-13a7 7 0 0 0-7-7zm0 9.5A2.5 2.5 0 1 1 12 6.5a2.5 2.5 0 0 1 0 5z"/></svg>
        <span>2876 Mellow Crest Lane<br>Irvine, CA 92611</span>
      </li>
      <li class="contact-item">
        <svg class="contact-icon" viewBox="0 0 24 24"><path d="M6.6 10.8a15.1 15.1 0 0 0 6.6 6.6l2.2-2.2a1 1 0 0 1 1-.25 11.4 11.4 0 0 0 3.6.57 1 1 0 0 1 1 1V20a1 1 0 0 1-1 1A17 17 0 0 1 3 4a1 1 0 0 1 1-1h3.5a1 1 0 0 1 1 1c0 1.25.2 2.45.57 3.6a1 1 0 0 1-.25 1z"/></svg>
        <span>012 555 0198</span>
      </li>
      <li class="contact-item">
        <svg class="contact-icon" viewBox="0 0 24 24"><path d="M6 3h9v5H6zM3 9h18v9h-3v3H6v-3H3zm5 6v4h8v-4z"/></svg>
        <span>012 555 0198</span>
      </li>
      <li class="contact-item">
        <svg class="contact-icon" viewBox="0 0 24 24"><path d="M2 5h20v14H2zm2 2v.5l8 5 8-5V7l-8 5z"/></svg>
        <span>tk@TheSolsticeLP.example</span>
      </li>
    </ul>

    <p class="website">www.TheSolsticeLP.example</p>
  </div>
</body>
</html>
```